Brochure - Silver Harbor Circle

We need a brochure (tri-fold or bi-fold) for our network marketing company, Silver Harbor Circle. The brochure will be used for our Promoters (Distributors) to hand out to prospective customers and Promoters explaining our service as well as the income opportunity.

Industry/Entity Type

Club

```html
<!DOCTYPE html>
<html lang="en">
<head>
<meta charset="utf-8">
<title>Silver Harbor Circle – Tri-fold Brochure</title>
<link rel="stylesheet" href="https://fonts.googleapis.com/css2?family=Ubuntu:wght@400;500;700&family=PT+Sans:wght@400;700&display=swap">
<style>
:root{
  --blue:#1b98d5;
  --blue-dark:#137cb8;
  --green:#7ac943;
  --green-dark:#5aa82a;
  --ink:#2f2f2f;
  --muted:#6a6a6a;
  --paper:#ffffff;
  --paper-shade:#eeeeee;
  --stage:#3a3a3a;
}
*{box-sizing:border-box;margin:0;padding:0}
html,body{width:1200px;height:1200px;overflow:hidden;background:var(--stage)}
body{position:relative;font-family:"PT Sans",Arial,sans-serif;color:var(--ink)}
.spread{position:absolute;left:195px;width:810px;height:560px;display:flex;box-shadow:0 6px 18px rgba(0,0,0,.45)}
.spread--outside{top:25px}
.spread--inside{top:615px}
.panel{position:relative;width:270px;height:560px;overflow:hidden;background:linear-gradient(90deg,var(--paper) 70%,var(--paper-shade))}
.panel--mid{background:linear-gradient(90deg,#e8e8e8,var(--paper) 30%,var(--paper) 75%,#ececec)}
.wave{position:absolute;left:0;bottom:0;width:810px;height:110px;pointer-events:none}

/* brand */
.brand{position:absolute;text-align:left;font-family:"Ubuntu",sans-serif}
.brand__name{display:flex;align-items:center;gap:6px;font-weight:700;color:var(--blue);font-size:26px;letter-spacing:-.5px;line-height:1}
.brand__dot{width:14px;height:14px;border-radius:50%;background:var(--green);flex:none}
.brand__sub{font-weight:400;color:var(--muted);font-size:14px;margin:2px 0 0 20px}
.brand--small .brand__name{font-size:23px}
.brand--small .brand__sub{font-size:13px}

/* pills & lists */
.pill{position:absolute;left:0;background:var(--blue);color:#fff;font-family:"Ubuntu",sans-serif;font-weight:700;font-size:12px;padding:4px 14px 4px 14px;border-radius:0 14px 14px 0}
.copy{position:absolute;left:15px;right:12px;font-size:10px;line-height:1.3}
.copy--justify{text-align:justify;font-size:8px;line-height:1.3}
.list{list-style:none;margin-top:6px}
.list li{display:flex;align-items:center;gap:10px;font-weight:700;font-size:10.5px;height:22.5px;padding-left:12px}
.bullet{width:15px;height:15px;border-radius:50%;background:var(--green);color:#fff;font-size:9px;display:flex;align-items:center;justify-content:center;flex:none;font-weight:700}
.seal{position:absolute;left:186px;top:262px;width:66px;height:66px;border-radius:50%;background:var(--blue);border:5px solid #e4f2fa;box-shadow:0 0 0 1px #bcdcef}
.photo{position:absolute}

/* contact */
.contact{position:absolute;left:0;right:0;text-align:center;font-size:12px}
.contact__icon{width:18px;height:18px;border-radius:50%;background:var(--green);margin:0 auto 5px;display:flex;align-items:center;justify-content:center}
.contact__item{margin-bottom:12px}
.contact__item--web{font-size:11px}

/* cover */
.cover__band{position:absolute;left:0;bottom:0;width:270px;height:125px}
.cover__title{position:absolute;left:0;right:0;text-align:center;font-family:"Ubuntu",sans-serif;font-weight:700;font-size:32px;line-height:1}
.cover__title--green{color:var(--green);top:472px}
.cover__title--white{color:#fff;top:512px}
.cover__url{position:absolute;left:0;right:0;top:550px;text-align:center;color:#fff;font-family:"Ubuntu",sans-serif;font-weight:700;font-size:8.5px}

/* steps */
.step{position:absolute;left:0;right:0}
.step__badge{position:absolute;width:44px;height:44px;border-radius:50%;background:var(--blue);border:3px solid #fff;box-shadow:0 0 0 1px #cfe6f3;color:#fff;font-family:"Ubuntu",sans-serif;text-align:center;line-height:1;z-index:2}
.step__badge small{display:block;font-size:10px;font-weight:500;margin-top:7px}
.step__badge b{display:block;font-size:17px}
.step__shot{position:absolute;border:1px solid #c8c8c8;background:#fff;font-size:5.5px;color:#555;overflow:hidden}
.step__title{position:absolute;left:0;right:0;text-align:center;color:var(--green-dark);font-family:"Ubuntu",sans-serif;font-weight:700;font-size:12.5px}
.step__text{position:absolute;left:12px;right:12px;font-size:7.5px;line-height:1.3;text-align:center}
.step__text--justify{text-align:justify}
.shot__bar{background:var(--green);color:#fff;font-weight:700;padding:3px 8px;font-size:5.5px}
.shot__select{border:1px solid #bbb;margin:4px 4px 2px;padding:1px 3px}
.shot__row{padding:1px 4px}
.shot__row--on{background:var(--blue);color:#fff}
.shot__price{font-family:"Ubuntu",sans-serif;font-weight:700;font-size:15px;color:var(--green-dark);text-align:center;margin-top:3px}

.soon{position:absolute;left:15px;top:226px;width:240px;height:160px;border:1.5px dashed #9fc98a;border-radius:8px;background:linear-gradient(180deg,#fafafa,#ececf0)}
.soon__pill{position:absolute;left:55px;top:-12px;width:130px;background:var(--blue);color:#fff;text-align:center;font-family:"Ubuntu",sans-serif;font-weight:700;font-size:12px;padding:4px 0;border-radius:12px}
</style>
</head>
<body>

<section class="spread spread--outside" aria-label="Brochure outside">
  <article class="panel panel--benefits">
    <div class="pill" style="top:20px">Benefits of becoming member</div>
    <div class="copy" style="top:50px">The benefits of becoming a Silver Harbor Circle Promoter, which are:
      <ul class="list">
        <li><span class="bullet">a</span>Earn Residual Income</li>
        <li><span class="bullet">b</span>Reclaim Your Time</li>
        <li><span class="bullet">c</span>Help People Save Money</li>
      </ul>
    </div>
    <div class="copy" style="top:158px">when becoming a Silver Harbor Circle Promoter, which are:
      <ul class="list">
        <li><span class="bullet">✓</span>Personalized Replicated Website</li>
        <li><span class="bullet">✓</span>Back-office Suite</li>
        <li><span class="bullet">✓</span>Personal Earnings Report</li>
        <li><span class="bullet">✓</span>Marketing Tools</li>
        <li><span class="bullet">✓</span>Team Telemetry</li>
        <li><span class="bullet">✓</span>Sales Training</li>
        <li><span class="bullet">✓</span>Technical Support</li>
      </ul>
    </div>
    <div class="seal" aria-hidden="true"></div>
    <div class="photo" role="img" aria-label="Group of four smiling decorators with a ladder, paint tins and rollers" style="left:0;top:345px;width:270px;height:185px;background:linear-gradient(180deg,#f4f4f4 0%,#e8e2da 55%,#c49a6c 100%)"></div>
  </article>

  <article class="panel panel--mid">
    <div class="brand brand--small" style="left:44px;top:178px">
      <div class="brand__name"><span class="brand__dot"></span>Silver Harbor</div>
      <div class="brand__sub">Home Services</div>
    </div>
    <div class="contact" style="top:255px">
      <div class="contact__item"><div class="contact__icon"><svg width="10" height="10" viewBox="0 0 10 10"><path d="M2 1l2 2-1 1.3c.6 1.2 1.5 2.1 2.7 2.7L7 6l2 2-1.3 1.3C4.5 9 1 5.5.7 2.3z" fill="#fff"/></svg></div>123-456-7890</div>
      <div class="contact__item"><div class="contact__icon"><svg width="10" height="8" viewBox="0 0 10 8"><rect x=".5" y=".5" width="9" height="7" fill="none" stroke="#fff"/><path d="M.5.5l4.5 4 4.5-4" fill="none" stroke="#fff"/></svg></div>hello@silverharbor.club</div>
      <div class="contact__item contact__item--web"><div class="contact__icon"><svg width="10" height="10" viewBox="0 0 10 10"><circle cx="5" cy="5" r="4" fill="none" stroke="#fff"/><path d="M1 5h8M5 1c-2 2.5-2 5.5 0 8M5 1c2 2.5 2 5.5 0 8" fill="none" stroke="#fff" stroke-width=".8"/></svg></div>silverharborhomes.club</div>
    </div>
  </article>

  <article class="panel panel--cover">
    <div class="photo" role="img" aria-label="Smiling woman in a green blouse working on a laptop on a white sofa" style="left:0;top:100px;width:270px;height:380px;background:linear-gradient(160deg,#f7efe0 0%,#efe3cf 35%,#9dd24f 60%,#5b4a3d 100%)"></div>
    <div class="brand" style="left:22px;top:28px">
      <div class="brand__name"><span class="brand__dot"></span>Silver Harbor</div>
      <div class="brand__sub">Home Services</div>
    </div>
    <svg class="cover__band" viewBox="0 0 270 125" preserveAspectRatio="none" aria-hidden="true">
      <path d="M0 22 C90 -6 190 0 270 30 L270 125 L0 125Z" fill="#fff"/>
      <path d="M0 28 C90 2 190 8 270 36 L270 125 L0 125Z" fill="var(--blue)"/>
    </svg>
    <div class="cover__title cover__title--green">Live Life</div>
    <div class="cover__title cover__title--white">at Your Price</div>
    <div class="cover__url">WWW.SILVERHARBORHOMES.CLUB</div>
  </article>

  <svg class="wave" viewBox="0 0 810 110" preserveAspectRatio="none" aria-hidden="true">
    <path d="M0 110 L0 70 C120 95 250 100 400 60 L540 10 L540 110Z" fill="var(--green)"/>
    <path d="M0 110 L0 82 C130 104 260 108 410 70 L540 22 L540 110Z" fill="#fff"/>
    <path d="M0 110 L0 92 C130 110 260 112 420 80 L540 40 L540 110Z" fill="#f4f4f4"/>
  </svg>
</section>

<section class="spread spread--inside" aria-label="Brochure inside">
  <article class="panel panel--process">
    <div class="pill" style="top:10px">Unique Process</div>
    <div class="copy copy--justify" style="top:36px">Here's the thing: you deserve to have quality work done by true professionals at a price you're happy about. That's one of the main reasons why we created this service: to give homeowners peace of mind. You name your price and take the hassle out of home projects, saving time and money.<br><br style="line-height:.5">We're not in the business of home services. We're just in the business of making your day. You're welcome.<br><br style="line-height:.5">View our process step by step</div>

    <div class="step" style="top:140px">
      <div class="step__badge" style="left:50px;top:0"><small>STEP</small><b>1</b></div>
      <div class="step__shot" style="left:95px;top:4px;width:100px;height:78px">
        <div class="shot__bar">GET STARTED NOW.</div>
        <div class="shot__select">Type or select a service ▾</div>
        <div class="shot__row shot__row--on">Appliance Repair</div>
        <div class="shot__row">Carpet Cleaning</div>
        <div class="shot__row">Chimney Sweep</div>
        <div class="shot__row">Countertops</div>
      </div>
      <div class="step__title" style="top:88px">Select your home service</div>
      <div class="step__text" style="top:105px">Pick your home service need from our extensive list of categories.</div>
    </div>

    <div class="step" style="top:268px">
      <div class="step__badge" style="left:50px;top:0"><small>STEP</small><b>2</b></div>
      <div class="step__shot" style="left:88px;top:6px;width:100px;height:74px;padding-top:12px">
        <div class="shot__row">Does not clean dishes</div>
        <div class="shot__row shot__row--on">Does not drain</div>
        <div class="shot__row">Does not dry dishes</div>
        <div class="shot__row">Does not work</div>
        <div class="shot__row">Door does not latch</div>
      </div>
      <div class="step__title" style="top:86px">Tell us about your project</div>
      <div class="step__text" style="top:103px">Complete our simple questionnaire to give us an idea of what your project needs are.</div>
    </div>

    <div class="step" style="top:396px">
      <div class="step__badge" style="left:50px;top:0"><small>STEP</small><b>3</b></div>
      <div class="step__shot" style="left:77px;top:6px;width:110px;height:70px;padding:6px 4px 0 22px;color:var(--blue);font-weight:700">Thanks, here is the average price your neighbors have paid:
        <div class="shot__price">$330.00</div>
      </div>
      <div class="step__title" style="top:81px">Get the average price</div>
      <div class="step__text step__text--justify" style="top:98px">Based on the information provided, you'll immediately see the average price for a project like yours – what others in your area are paying, on average, for the same type of project.</div>
    </div>
  </article>

  <article class="panel panel--mid">
    <div class="step" style="top:12px">
      <div class="step__badge" style="left:48px;top:2px"><small>STEP</small><b>4</b></div>
      <div class="step__shot" style="left:75px;top:4px;width:120px;height:70px;background:#333;border-color:#333;color:#ddd;padding:6px 6px 0 20px"><span style="color:var(--blue);font-weight:700">Silver Harbor</span><br>Name your price here<div style="margin-top:8px;height:12px;width:70px;border-radius:6px;background:#fff;border:2px solid var(--blue)"></div></div>
      <div class="step__title" style="top:100px">Name your price!</div>
      <div class="step__text step__text--justify" style="top:118px">Taking the average price for this project into consideration, you now get to name your own price. Be as conservative or as bold as you wish. Or somewhere in between, it's totally up to you.</div>
    </div>

    <div class="step" style="top:180px">
      <div class="step__badge" style="left:42px;top:0"><small>STEP</small><b>5</b></div>
      <div class="photo" role="img" aria-label="Three service professionals standing in front of a house" style="left:65px;top:4px;width:130px;height:92px;background:linear-gradient(180deg,#e9d79a,#c9b07a 50%,#6b6e63)"></div>
      <div class="step__title" style="top:103px">Your offer is distributed</div>
      <div class="step__text step__text--justify" style="top:118px">We'll immediately send your price to our network of qualified, pre-screened service pros in your area. They immediately begin to arm wrestle for it.</div>
    </div>

    <div class="step" style="top:350px">
      <div class="step__badge" style="left:40px;top:0"><small>STEP</small><b>6</b></div>
      <div class="photo" role="img" aria-label="Happy woman relaxing on a green sofa with a laptop" style="left:65px;top:4px;width:125px;height:90px;background:linear-gradient(180deg,#f0f0f0 0%,#dfe6e8 55%,#6fbf44 100%)"></div>
      <div class="step__title" style="top:100px">Your Price is Accepted</div>
      <div class="step__text step__text--justify" style="top:117px">Within 60 minutes, you will be notified when one of our service pros accepts your price. The service pro will then contact you directly to set up your appointment.</div>
    </div>
  </article>

  <article class="panel panel--about">
    <div class="brand" style="left:32px;top:10px">
      <div class="brand__name"><span class="brand__dot"></span>Silver Harbor</div>
      <div class="brand__sub">Home Services</div>
    </div>
    <div class="copy copy--justify" style="top:78px;left:8px;right:10px">a. Silver Harbor Circle's innovative model combines the bulk savings idea of Bulkway Club; with the "name your own price" concept of RateBid.com to fill provider vacancies. A win-win for consumers and service providers alike, Silver Harbor Circle empowers Member consumers with fair market rate information for home improvement, maintenance and repair services; and then enables them to name their own price to submit to a network of pre-screened, local service professionals who have vacancies in their schedules that they are willing to fill at the Member's submitted price.</div>
    <div class="soon">
      <div class="soon__pill">Coming Soon</div>
      <div class="brand brand--small" style="left:24px;top:28px">
        <div class="brand__name"><span class="brand__dot"></span>Silver Harbor</div>
        <div class="brand__sub">Auto Services</div>
      </div>
      <div class="brand brand--small" style="left:24px;top:90px">
        <div class="brand__name"><span class="brand__dot"></span>Silver Harbor</div>
        <div class="brand__sub">Life &amp; Learning</div>
      </div>
    </div>
    <div class="photo" role="img" aria-label="Smiling couple giving thumbs up" style="left:0;top:390px;width:270px;height:170px;background:linear-gradient(180deg,#fafafa 0%,#e7c9ad 40%,#4a8fd0 100%)"></div>
  </article>

  <svg class="wave" viewBox="0 0 810 110" preserveAspectRatio="none" aria-hidden="true">
    <path d="M0 110 L0 104 C200 104 420 96 600 66 C680 50 740 28 810 30 L810 38 C740 38 690 58 610 75 C430 104 200 109 0 109Z" fill="var(--green)"/>
  </svg>
</section>

</body>
</html>
```